Business Card *

A business card design
Use the logo uploaded in the brief page.
You may use placeholders in your design layouts.
I will provide the actual business card details to the winning designer.

Logo
Place for contact info (name, title, phone, email, etc)

Requirements
Must have
• Logo

```html
<!DOCTYPE html>
<html lang="en">
<head>
<meta charset="utf-8">
<title>Kestrelby Business Card</title>
<link rel="stylesheet" href="https://fonts.googleapis.com/css2?family=Montserrat:wght@400;500;700&display=swap">
<style>
  :root {
    --backdrop: #141414;
    --card: #1c1c1c;
    --card-edge: #262626;
    --ink-light: #e6e6e6;
    --ink-muted: #b9b9b9;
    --brand-green: #6cc04a;
    --emboss: #262626;
    --emboss-light: #2f2f2f;
  }
  * { margin: 0; padding: 0; box-sizing: border-box; }
  html, body {
    width: 1200px;
    height: 711px;
    overflow: hidden;
    background: var(--backdrop);
    font-family: "Montserrat", sans-serif;
  }
  .stage {
    width: 1200px;
    height: 711px;
    display: flex;
    align-items: center;
    justify-content: center;
    gap: 60px;
  }
  .card {
    width: 525px;
    height: 300px;
    background: var(--card);
    border-radius: 3px;
    box-shadow: 0 0 0 1px var(--card-edge), 0 18px 40px rgba(0,0,0,0.6);
    position: relative;
    overflow: hidden;
  }
  /* front */
  .card-front {
    display: flex;
    align-items: center;
  }
  .brand {
    width: 50%;
    display: flex;
    align-items: center;
    justify-content: center;
    gap: 12px;
  }
  .brand-dot {
    width: 30px;
    height: 30px;
    border-radius: 50%;
    background: var(--brand-green);
  }
  .brand-name {
    font-weight: 700;
    font-size: 26px;
    letter-spacing: 1px;
    color: var(--ink-light);
    text-transform: uppercase;
  }
  .contact {
    width: 50%;
    padding-left: 20px;
  }
  .contact-name {
    font-size: 19px;
    font-weight: 500;
    letter-spacing: 1.5px;
    color: var(--ink-light);
  }
  .contact-title {
    font-size: 12px;
    font-weight: 500;
    letter-spacing: 2px;
    color: var(--brand-green);
    margin-top: 3px;
    margin-bottom: 16px;
  }
  .contact-list { list-style: none; }
  .contact-item {
    display: flex;
    align-items: center;
    gap: 9px;
    font-size: 11.5px;
    color: var(--ink-muted);
    margin-bottom: 8px;
  }
  .contact-icon {
    width: 12px;
    height: 12px;
    flex: none;
  }
  /* back */
  .card-back {
    display: flex;
    align-items: center;
    justify-content: center;
  }
  .emboss-mark {
    display: flex;
    align-items: center;
    gap: 16px;
  }
  .emboss-circle {
    width: 110px;
    height: 110px;
    border-radius: 50%;
    border: 3px solid var(--emboss);
    box-shadow: inset 1px 1px 0 var(--emboss-light), 1px 1px 0 var(--emboss-light);
  }
  .emboss-name {
    font-weight: 700;
    font-size: 30px;
    letter-spacing: 1px;
    color: var(--emboss);
    text-shadow: 1px 1px 0 var(--emboss-light);
    text-transform: uppercase;
  }
</style>
</head>
<body>
<main class="stage">
  <section class="card card-front">
    <div class="brand">
      <span class="brand-dot"></span>
      <span class="brand-name">Kestrelby</span>
    </div>
    <div class="contact">
      <p class="contact-name">YOUR NAME</p>
      <p class="contact-title">JOB TITLE</p>
      <ul class="contact-list">
        <li class="contact-item">
          <svg class="contact-icon" viewBox="0 0 12 12" aria-hidden="true">
            <path d="M2.5 1 L4.5 1 L5 3.5 L3.8 4.4 A6 6 0 0 0 7.6 8.2 L8.5 7 L11 7.5 L11 9.5 A1.5 1.5 0 0 1 9.5 11 A8.5 8.5 0 0 1 1 2.5 A1.5 1.5 0 0 1 2.5 1 Z" fill="var(--brand-green)"/>
          </svg>
          000 000 0000
        </li>
        <li class="contact-item">
          <svg class="contact-icon" viewBox="0 0 12 12" aria-hidden="true">
            <rect x="0.5" y="2" width="11" height="8" rx="1" fill="var(--brand-green)"/>
            <path d="M1 2.5 L6 6.5 L11 2.5" stroke="var(--card)" stroke-width="1" fill="none"/>
          </svg>
          youremail@xyz.com
        </li>
        <li class="contact-item">
          <svg class="contact-icon" viewBox="0 0 12 12" aria-hidden="true">
            <circle cx="6" cy="6" r="5.5" fill="var(--brand-green)"/>
            <path d="M0.5 6 H11.5 M6 0.5 V11.5 M6 0.5 C3 3 3 9 6 11.5 M6 0.5 C9 3 9 9 6 11.5" stroke="var(--card)" stroke-width="0.8" fill="none"/>
          </svg>
          www.yourwebsite.com
        </li>
      </ul>
    </div>
  </section>
  <section class="card card-back">
    <div class="emboss-mark">
      <span class="emboss-circle"></span>
      <span class="emboss-name">Kestrelby</span>
    </div>
  </section>
</main>
</body>
</html>
```